Real estate Agent postcards for homeowners

I need a "Just Sold" postcard for two real agents , I am providing pictures of the agents and neighborhood.
I have the front and back of a postcard containing the information I want on the postcard.
I want a designer to take the info and pictures and design a new postcard and choose the colors

Target Market(s)

homeowners of luxury condos

Industry/Entity Type

Real Estate Agent

Colors

Designer to choose colors to be used in the design.

```html
<!DOCTYPE html>
<html lang="en">
<head>
<meta charset="utf-8">
<title>Harborline Realtors – Just Sold Postcard</title>
<link href="https://fonts.googleapis.com/css2?family=Anton&family=EB+Garamond:wght@400;600;700&display=swap" rel="stylesheet">
<style>
:root{
  --red:#d3161f;
  --red-dark:#a80f16;
  --yellow:#ffd800;
  --gold:#e2bd0b;
  --ink:#262626;
  --panel:#2b2b2b;
  --paper:#ffffff;
  --mist:#eceef0;
  --bg:#e4e1dc;
}
*{box-sizing:border-box;margin:0;padding:0}
html,body{width:1200px;height:1200px;overflow:hidden;background:var(--bg)}
body{position:relative;font-family:"EB Garamond",Georgia,serif}
.card{position:absolute;left:210px;width:780px;height:540px;background:var(--paper);overflow:hidden;box-shadow:0 6px 18px rgba(0,0,0,.25)}
.card--front{top:40px}
.card--back{top:620px}
.card svg.shapes{position:absolute;inset:0}
.abs{position:absolute;white-space:nowrap}
.display{font-family:"Anton",Impact,sans-serif;letter-spacing:.5px}
.brand{font-family:"EB Garamond",Georgia,serif;color:#fff;font-weight:600;text-transform:uppercase}
/* front */
.front__brand{left:528px;top:28px;font-size:19px;line-height:1}
.front__headline{left:525px;top:74px;font-size:46px;color:var(--yellow);line-height:1}
.front__place{left:520px;top:140px;font-size:28px;color:#fff;line-height:1}
.listing{left:522px;color:#fff;font-size:14px;line-height:1.25}
.listing .tick{display:inline-block;width:12px;height:12px;margin-right:5px;vertical-align:-1px}
.listing .price{color:var(--yellow);font-weight:700;font-size:19px}
.listing .side{font-size:13px}
.listing .indent{padding-left:17px}
.front__tagline{left:0;top:345px;width:780px;height:48px;line-height:48px;text-align:center;font-size:25px;color:var(--ink);font-weight:600}
.agent-name{font-size:23px;color:var(--yellow);line-height:1}
.agent-line{font-size:15px;color:var(--ink);line-height:1.6}
.agent-line .ico{display:inline-block;width:12px;height:12px;margin-right:7px;vertical-align:-1px}
.unit{font-weight:700;font-size:15px;margin-top:4px;color:var(--ink)}
/* back */
.back__brand{left:36px;top:30px;font-size:25px;line-height:1}
.back__address{left:36px;top:66px;font-size:14px;color:#fff}
.back__heading{left:36px;top:104px;font-size:22px;color:#fff;line-height:1.15}
.back__copy{left:36px;top:158px;font-size:16px;color:#fff;line-height:1.55}
.back__copy .web{color:var(--yellow);font-weight:700;font-size:19px}
.back-agent .agent-name{color:#1e1e1e;font-size:22px}
.back-agent .agent-line{color:#1e1e1e;font-size:14px;line-height:1.5}
.license{left:170px;top:494px;color:#fff;font-size:15px;letter-spacing:.5px}
.disclaimer{right:22px;top:490px;font-size:10.5px;color:var(--ink);text-align:right;line-height:1.3}
</style>
</head>
<body>

<section class="card card--front">
  <svg class="shapes" width="780" height="540" viewBox="0 0 780 540">
    <defs>
      <linearGradient id="coastTone" x1="0" y1="0" x2="0" y2="1">
        <stop offset="0" stop-color="#8fbde6"/>
        <stop offset=".38" stop-color="#2f6fa8"/>
        <stop offset=".62" stop-color="#5c9a3f"/>
        <stop offset="1" stop-color="#8a5a3a"/>
      </linearGradient>
      <linearGradient id="portraitWarm" x1="0" y1="0" x2="0" y2="1">
        <stop offset="0" stop-color="#b89a72"/><stop offset="1" stop-color="#e3c79a"/>
      </linearGradient>
      <linearGradient id="portraitSea" x1="0" y1="0" x2="0" y2="1">
        <stop offset="0" stop-color="#6aa4d8"/><stop offset="1" stop-color="#2d4f7c"/>
      </linearGradient>
    </defs>
    <rect class="photo" x="0" y="0" width="510" height="345" fill="url(#coastTone)" role="img" aria-label="Photo of oceanfront condos with lawn and flowering gardens above the bay"/>
    <polygon class="dark-panel" points="485,0 780,0 780,345 485,345 505,110" fill="var(--panel)"/>
    <polygon class="ribbon-tail" points="455,95 490,82 490,140 470,140" fill="var(--red-dark)"/>
    <polygon class="ribbon" points="485,72 780,62 780,122 485,132" fill="var(--red)"/>
    <line x1="485" y1="66" x2="780" y2="56" stroke="#ddd" stroke-width="2"/>
    <line x1="485" y1="136" x2="780" y2="126" stroke="#ddd" stroke-width="2"/>
    <rect class="tagline-band" x="0" y="345" width="780" height="48" fill="var(--yellow)"/>
    <rect class="agent-area" x="0" y="393" width="780" height="147" fill="var(--mist)"/>
    <rect x="30" y="405" width="115" height="125" fill="var(--red)"/>
    <rect x="35" y="410" width="105" height="115" fill="url(#portraitWarm)" role="img" aria-label="Portrait of agent Maren Holloway"/>
    <polygon points="145,405 330,405 318,420 330,435 145,435" fill="var(--red)"/>
    <rect x="420" y="405" width="115" height="125" fill="var(--red)"/>
    <rect x="425" y="410" width="105" height="115" fill="url(#portraitSea)" role="img" aria-label="Portrait of agent Theo Varga"/>
    <polygon points="535,405 690,405 678,420 690,435 535,435" fill="var(--red)"/>
  </svg>

  <div class="abs brand front__brand">Harborline Realtors</div>
  <div class="abs display front__headline">JUST SOLD!</div>
  <div class="abs display front__place">IN SEABRIGHT COVE</div>

  <div class="abs listing" style="top:178px">
    <div><svg class="tick" viewBox="0 0 12 12"><rect x=".5" y="2.5" width="9" height="9" fill="none" stroke="#ffd800"/><path d="M2 6l3 3 6-8" fill="none" stroke="#ffd800" stroke-width="2"/></svg>43 Costa Linda in Building 13</div>
    <div class="indent">3 bedrooms, 2 bathroom, 1840 sq ft</div>
    <div class="indent">Sold for</div>
    <div class="indent"><span class="price">$1,000,000</span> <span class="side">buyer side</span></div>
  </div>
  <div class="abs listing" style="top:262px">
    <div><svg class="tick" viewBox="0 0 12 12"><rect x=".5" y="2.5" width="9" height="9" fill="none" stroke="#ffd800"/><path d="M2 6l3 3 6-8" fill="none" stroke="#ffd800" stroke-width="2"/></svg>80 Costa Linda in Building 8</div>
    <div class="indent">1 bedroom, 2 bathroom, 985 sq ft</div>
    <div class="indent">Sold for</div>
    <div class="indent"><span class="price">$769,000</span> <span class="side">seller side</span></div>
  </div>

  <div class="abs front__tagline">We are local agents and your neighbors! Call us for more information!</div>

  <div class="abs display agent-name" style="left:155px;top:409px">MAREN HOLLOWAY</div>
  <div class="abs" style="left:155px;top:444px">
    <div class="agent-line"><svg class="ico" viewBox="0 0 12 12"><path d="M2 1l2.5 0 1 3-1.5 1c.7 1.5 1.5 2.3 3 3l1-1.5 3 1V11C5 11 1 7 1 2z" fill="#d3161f"/></svg>(310) 555-0142</div>
    <div class="agent-line"><svg class="ico" viewBox="0 0 12 12"><rect x=".5" y="2" width="11" height="8" fill="#d3161f"/><path d="M.5 2l5.5 4.5L11.5 2" fill="none" stroke="#fff"/></svg>HomesbyMaren@mail.com</div>
    <div class="unit">UNIT 18-70</div>
  </div>

  <div class="abs display agent-name" style="left:545px;top:409px">THEO VARGA</div>
  <div class="abs" style="left:545px;top:444px">
    <div class="agent-line"><svg class="ico" viewBox="0 0 12 12"><path d="M2 1l2.5 0 1 3-1.5 1c.7 1.5 1.5 2.3 3 3l1-1.5 3 1V11C5 11 1 7 1 2z" fill="#d3161f"/></svg>(650) 555-0187</div>
    <div class="agent-line"><svg class="ico" viewBox="0 0 12 12"><rect x=".5" y="2" width="11" height="8" fill="#d3161f"/><path d="M.5 2l5.5 4.5L11.5 2" fill="none" stroke="#fff"/></svg>TheoVarga@mail.com</div>
    <div class="unit">UNIT 8-84</div>
  </div>
</section>

<section class="card card--back">
  <svg class="shapes" width="780" height="540" viewBox="0 0 780 540">
    <defs>
      <linearGradient id="redField" x1="0" y1="0" x2="1" y2="1">
        <stop offset="0" stop-color="#d81a22"/><stop offset="1" stop-color="#b8121a"/>
      </linearGradient>
      <linearGradient id="portraitWarm2" x1="0" y1="0" x2="0" y2="1">
        <stop offset="0" stop-color="#b89a72"/><stop offset="1" stop-color="#e3c79a"/>
      </linearGradient>
      <linearGradient id="portraitSea2" x1="0" y1="0" x2="0" y2="1">
        <stop offset="0" stop-color="#6aa4d8"/><stop offset="1" stop-color="#2d4f7c"/>
      </linearGradient>
    </defs>
    <polygon class="stripe-black" points="0,0 375,0 470,185 360,540 0,540" fill="var(--ink)"/>
    <polygon class="stripe-yellow" points="0,0 358,0 453,185 343,540 0,540" fill="var(--yellow)"/>
    <polygon class="red-field" points="0,0 343,0 438,185 328,540 0,540" fill="url(#redField)"/>
    <line x1="36" y1="91" x2="395" y2="84" stroke="#fff" stroke-opacity=".5"/>
    <polygon points="150,232 418,220 392,330 150,338" fill="var(--gold)"/>
    <polygon points="150,366 385,358 350,462 150,470" fill="var(--gold)"/>
    <rect x="48" y="226" width="112" height="124" rx="6" fill="#fff"/>
    <rect x="53" y="231" width="102" height="114" rx="4" fill="url(#portraitWarm2)" role="img" aria-label="Portrait of agent Maren Holloway"/>
    <rect x="48" y="360" width="112" height="124" rx="6" fill="#fff"/>
    <rect x="53" y="365" width="102" height="114" rx="4" fill="url(#portraitSea2)" role="img" aria-label="Portrait of agent Theo Varga"/>
    <rect class="badge" x="62" y="490" width="76" height="36" fill="#fff" stroke="#222" stroke-width="1.5"/>
    <rect class="stamp-box" x="688" y="25" width="64" height="80" fill="#fff" stroke="#999"/>
  </svg>

  <div class="abs brand back__brand">Harborline Realtors</div>
  <div class="abs back__address"><svg width="11" height="13" viewBox="0 0 11 13" style="vertical-align:-1px;margin-right:6px"><path d="M5.5 0A5 5 0 0 0 .5 5c0 3.5 5 8 5 8s5-4.5 5-8a5 5 0 0 0-5-5z" fill="#ffd800"/><circle cx="5.5" cy="5" r="2" fill="#c8141c"/></svg>210 Harbor View Rd SEABRIGHT, CA 90001-2400</div>
  <div class="abs display back__heading">WE ARE SEABRIGHT AGENTS AND YOUR<br>SEABRIGHT COVE NEIGHBORS.</div>
  <div class="abs back__copy">Call us for a free property market evaluation.<br>Visit Us At <span class="web">www.HarborlineRealtors.com</span></div>

  <div class="abs back-agent" style="left:172px;top:238px">
    <div class="display agent-name">MAREN HOLLOWAY</div>
    <div class="agent-line" style="margin-top:4px"><svg class="ico" viewBox="0 0 12 12"><path d="M2 1l2.5 0 1 3-1.5 1c.7 1.5 1.5 2.3 3 3l1-1.5 3 1V11C5 11 1 7 1 2z" fill="#d3161f"/></svg>(310) 555-0142</div>
    <div class="agent-line"><svg class="ico" viewBox="0 0 12 12"><rect x=".5" y="2" width="11" height="8" fill="#d3161f"/><path d="M.5 2l5.5 4.5L11.5 2" fill="none" stroke="#fff"/></svg>HomesbyMaren@mail.com</div>
    <div class="agent-line">BRE# 01234567</div>
  </div>
  <div class="abs back-agent" style="left:172px;top:372px">
    <div class="display agent-name">THEO VARGA</div>
    <div class="agent-line" style="margin-top:4px"><svg class="ico" viewBox="0 0 12 12"><path d="M2 1l2.5 0 1 3-1.5 1c.7 1.5 1.5 2.3 3 3l1-1.5 3 1V11C5 11 1 7 1 2z" fill="#d3161f"/></svg>(650) 555-0187</div>
    <div class="agent-line"><svg class="ico" viewBox="0 0 12 12"><rect x=".5" y="2" width="11" height="8" fill="#d3161f"/><path d="M.5 2l5.5 4.5L11.5 2" fill="none" stroke="#fff"/></svg>TheoVarga@mail.com</div>
    <div class="agent-line">BRE# 00765432</div>
  </div>

  <div class="abs license">CALBRE # 00815273</div>
  <div class="abs disclaimer">If your property is already listed with a broker, please disregard this mailing.<br>This is not a solicitation</div>
</section>

</body>
</html>
```